someone who can choose good colours and fonts and a style for an already layed out web page

HI

We need someone who can choose good colors and fonts and style for an already layed out web page.

please look at the first file.

The hard part of what needs to go where is already done,

1) we just need a type of character suitable for our business

2) colors probably in the green / yellow spectrum to suit our business

3) we need you to choose the style. For example you could choose round photos, or square buttons, video boxes with or without frames, that sort of stuff, just tweaking of what is there. plain arial is probably what we'd like but with text but with script or memorable headings. We would just like a design style that you think would be good gor our business model.

4) the twitter,facebook logo needs to be put in a new place

our project is an Italian style village in Italy called "Casale Delle Rondini", in Abruzzo, Italy.
It is surrounded by vineyards, lake and olive trees.

The most important is that it looks expensive, the village is eco friendly so anything on those lines is great, Obviously Italian, so italian looking characters

our website is www.collinetorre.com but we are updating it. we like the style of the old site , but it is too out of date

you can create the layout using the files we've given below and boxes
Updates

hi we've just updated out brief to make it more simple, its actually not much work its just about design choices

Target Market(s)

all lovers of Italian things
eco frienly

Industry/Entity Type

Business

Font styles to use
Decorative
Script

Colors
fcf9ce
faee3f
fde18a
fece3e
cadf82
9bcb3b
acd036
fce7d2
ec2027

Requirements
Must have
• has to have the same layout or similar so as all the boxes and links are in there
twitter,facebook and other logos need to be present where you want them
Nice to have
• we have chosen some colors but you can choose others 3 or 4 are usual a good number with a light yellow background maybe....
Should not have
• no old style must look up to date

```html
<!DOCTYPE html>
<html lang="en">
<head>
<meta charset="utf-8">
<title>Casale Delle Rondini</title>
<link href="https://fonts.googleapis.com/css2?family=Open+Sans:wght@400;600;700&display=swap" rel="stylesheet">
<style>
:root{
  --green:#8cc63f;
  --green-dark:#6fae22;
  --green-text:#7aab1f;
  --cream:#fcf9ce;
  --cream-soft:#fdf8dc;
  --yellow:#fece3e;
  --yellow-light:#fde18a;
  --orange:#f9b928;
  --red:#ec2027;
  --ink:#222;
  --grey:#777;
  --white:#fff;
}
*{margin:0;padding:0;box-sizing:border-box}
html,body{width:834px;height:1200px;overflow:hidden;background:var(--white)}
body{position:relative;font-family:'Open Sans',Arial,sans-serif;color:var(--ink)}
.abs{position:absolute}
a{color:inherit;text-decoration:none}

/* header */
.site-header{left:0;top:0;width:834px;height:100px;background:var(--white)}
.brand{left:50px;top:14px;display:flex;align-items:center;gap:14px}
.brand-mark{width:70px;height:70px;border-radius:50%;background:var(--green)}
.brand-name{font-size:34px;font-weight:400;color:#1d1d1d;letter-spacing:.2px}
.contact{right:50px;top:28px;text-align:right}
.phone{display:flex;align-items:center;justify-content:flex-end;gap:6px;font-size:20px;color:var(--green-dark)}
.address{font-size:10.5px;color:var(--green-dark);margin-top:2px}
.social-top{display:flex;gap:6px;justify-content:flex-end;margin-top:6px;padding-right:38px}
.social-top span{width:17px;height:17px;border-radius:2px;display:block}

/* nav */
.main-nav{left:0;top:101px;width:834px;height:40px;background:linear-gradient(#a6d653,#7fbf2a);border-top:1px solid #6aa51f}
.main-nav ul{list-style:none;display:flex;height:100%;padding-left:24px}
.main-nav li{color:var(--white);font-size:13.5px;padding:0 14px;line-height:40px;border-right:1px solid rgba(255,255,255,.35)}
.main-nav li:last-child{border-right:0}

/* hero */
.hero{left:0;top:141px;width:834px;height:344px;background:var(--cream);border-bottom:1px solid #e4dfa8}
.site-map{left:45px;top:9px;width:433px;height:335px;background:linear-gradient(135deg,#d8eba0,#9ccc48 55%,#f4f1c8)}
.themes{left:485px;top:11px;display:flex;gap:2px}
.theme{width:60px;height:95px;background:var(--yellow-light)}
.theme .ph{height:65px}
.theme p{font-size:8.5px;line-height:10.5px;color:#8a6a10;padding:3px 6px}
.slider{left:485px;top:114px;width:309px;height:221px;background:var(--orange);padding:7px 8px}
.slide-main{width:293px;height:158px;border:2px solid var(--white);background:linear-gradient(160deg,#3f8f1e,#7cc23a 55%,#9a9a88)}
.slide-strip{display:flex;align-items:center;gap:2px;margin-top:8px}
.slide-strip .arrow{width:10px;color:var(--ink);font-size:14px;text-align:center}
.slide-strip .thumb{width:52px;height:38px}

/* intro */
.intro{left:40px;top:514px;width:754px;text-align:center}
.intro h1{font-size:18px;font-weight:400;color:#111;margin-bottom:6px}
.intro p{font-size:9.3px;line-height:16px;color:var(--grey)}

/* promo row */
.promo-band{left:0;top:652px;width:834px;height:138px;background:repeating-linear-gradient(135deg,#eee 0 1px,#fff 1px 4px)}
.newsletter{left:40px;top:652px;width:228px;height:138px;background:linear-gradient(#ee3a3f,var(--red));padding:18px 21px;color:var(--white)}
.newsletter h2{font-size:19px;font-weight:400}
.newsletter small{font-size:8.5px;display:block;margin-top:3px}
.newsletter .field{margin-top:8px;height:24px;background:var(--white);color:#666;font-size:9px;padding:5px 9px}
.newsletter .btn{position:absolute;right:7px;bottom:20px;width:91px;height:26px;background:linear-gradient(#fee07a,var(--yellow));color:#3a2a00;font-size:11px;font-weight:700;text-align:center;line-height:26px;border-radius:2px}
.seasons{left:272px;top:652px;width:290px;height:138px;list-style:none}
.seasons li{height:34.5px;display:flex;align-items:center;padding-left:24px;gap:14px;font-size:12px;color:#6b4c00;position:relative}
.seasons li:nth-child(odd){background:var(--yellow)}
.seasons li:nth-child(even){background:var(--yellow-light)}
.seasons li::after{content:"";position:absolute;right:14px;width:10px;height:10px;border-top:1px solid #a07a10;border-right:1px solid #a07a10;transform:rotate(45deg)}
.book-trip{left:566px;top:652px;width:228px;height:138px;background:linear-gradient(#6fa83a,#7ec44a 55%,#8ccf57)}
.book-trip .bar{position:absolute;left:0;bottom:0;width:100%;height:36px;background:rgba(30,40,20,.72);display:flex;align-items:center;justify-content:space-between;padding:0 12px 0 15px}
.book-trip .bar span{color:var(--white);font-size:16px}
.book-trip .bar b{background:linear-gradient(#fee07a,var(--yellow));color:#3a2a00;font-size:9.5px;padding:5px 14px;border-radius:2px}

/* blog & videos */
.section-title{font-size:15px;font-weight:600}
.t-green{color:var(--green-text)}
.t-red{color:var(--red)}
.post{width:172px}
.post .img{height:80px;margin-top:10px}
.post h3{font-size:10px;font-weight:400;color:#333;margin-top:7px}
.post p{font-size:9px;line-height:16px;color:var(--grey);margin-top:2px}
.video{width:183px;height:147px;border:1px solid #ddd;padding:4px;background:var(--white);box-shadow:0 1px 2px rgba(0,0,0,.08)}
.video .img{width:100%;height:100%;position:relative}
.play{position:absolute;left:50%;top:50%;width:30px;height:30px;margin:-15px 0 0 -15px}

/* links band */
.more-sites{left:0;top:1017px;width:834px;height:96px;background:var(--cream-soft)}
.more-sites h2{font-size:12.5px;font-weight:400;color:#333;text-align:center;margin-top:20px}
.site-links{display:grid;grid-template-columns:repeat(5,158.5px);padding-left:45px;margin-top:7px;row-gap:6px}
.site-links span{font-size:8.6px;font-weight:600;color:#444;display:flex;align-items:center;gap:4px}
.site-links span::before{content:"";border-left:5px solid #333;border-top:4px solid transparent;border-bottom:4px solid transparent}

/* footer */
.site-footer{left:0;top:1113px;width:834px;height:87px;background:linear-gradient(#86bd30,#7ab42a)}
.footer-nav{left:42px;top:24px;font-size:11px;color:var(--white)}
.footer-nav i{font-style:normal;margin:0 6px;opacity:.9}
.copyright{left:42px;top:48px;font-size:9.5px;color:#e6f3cc}
.social-foot{right:44px;top:21px;display:flex;gap:3px}
.social-foot span{width:21px;height:21px;border-radius:50%;background:var(--white);display:block}
</style>
</head>
<body>

<header class="abs site-header">
  <div class="abs brand">
    <span class="brand-mark"></span>
    <span class="brand-name">Casale Delle Rondini</span>
  </div>
  <div class="abs contact">
    <div class="phone">
      <svg width="16" height="16" viewBox="0 0 24 24" aria-hidden="true"><path d="M6.6 10.8a15 15 0 0 0 6.6 6.6l2.2-2.2a1 1 0 0 1 1-.25 11.4 11.4 0 0 0 3.6.57 1 1 0 0 1 1 1V20a1 1 0 0 1-1 1A17 17 0 0 1 3 4a1 1 0 0 1 1-1h3.5a1 1 0 0 1 1 1c0 1.25.2 2.45.57 3.57a1 1 0 0 1-.25 1z" fill="#bbb"/></svg>
      085 555 0142
    </div>
    <div class="address">Via dei Tigli 12 Collemare</div>
    <div class="social-top" aria-label="Social links">
      <span style="background:#c9302c"></span>
      <span style="background:#3b5998"></span>
      <span style="background:#55c3ee"></span>
    </div>
  </div>
</header>

<nav class="abs main-nav">
  <ul>
    <li>HOME</li><li>WHICH REASON</li><li>ABOUT</li><li>PRICE LIST</li><li>VIDEOS</li><li>BLOG</li><li>PHOTOS</li><li>BOOK TRIP</li><li>CONTACT</li>
  </ul>
</nav>

<section class="abs hero">
  <div class="abs site-map" role="img" aria-label="Site plan of the village showing phases A to D, villas, lake, olive groves and playground"></div>
  <div class="abs themes">
    <div class="theme"><div class="ph" role="img" aria-label="Sunflower in the sun" style="background:linear-gradient(#4f9be0,#f1c21b)"></div><p>In the Sun</p></div>
    <div class="theme"><div class="ph" role="img" aria-label="Sandy beach" style="background:linear-gradient(#e8c9a2,#b98a5c)"></div><p>by the Beach</p></div>
    <div class="theme"><div class="ph" role="img" aria-label="Snowy mountain under blue sky" style="background:linear-gradient(#2b4f9a,#d8dfe8)"></div><p>Sky in Mountain</p></div>
    <div class="theme"><div class="ph" role="img" aria-label="Olive grove" style="background:linear-gradient(#a7b38a,#4e6b2a)"></div><p>BBQ in olive green</p></div>
    <div class="theme"><div class="ph" role="img" aria-label="Ancient Roman amphitheatre" style="background:linear-gradient(#3d6fb5,#b4803e)"></div><p>Near Rome</p></div>
  </div>
  <div class="abs slider">
    <div class="slide-main" role="img" aria-label="Tree-lined park path"></div>
    <div class="slide-strip">
      <span class="arrow">&#8249;</span>
      <span class="thumb" role="img" aria-label="Park lawn" style="background:linear-gradient(#a8cf6a,#4c8f2a)"></span>
      <span class="thumb" role="img" aria-label="Flower garden" style="background:linear-gradient(#6d9a3a,#b87a3a)"></span>
      <span class="thumb" role="img" aria-label="Garden path" style="background:linear-gradient(#3f8a2a,#a5c06c)"></span>
      <span class="thumb" role="img" aria-label="Autumn trees" style="background:linear-gradient(#e2b23a,#b8861c)"></span>
      <span class="thumb" role="img" aria-label="Leafy tree" style="background:linear-gradient(#dfeed3,#4c8a2a)"></span>
      <span class="arrow">&#8250;</span>
    </div>
  </div>
</section>

<section class="abs intro">
  <h1>Casale Delle Rondini is built in traditional Italian architectural style and surrounded by olive groves,</h1>
  <p>vineyards, a beautiful lake surrounded by a park with wildlife. The panoramic view of the mountains is breathtaking and you can see for 30 miles on a clear day. Red and white umbrellas, barbeques, swimming pools and a spa will contribute to its unique atmosphere. there will also be a health farm, where you can treat yourself to a luxurious massage. Ten shops and ensure any of your other needs can be met. Casale Delle Rondini is ensconced in the beauty of the Italian countryside,<br>where the hot white sandy beaches of the Adriatic coastline meet the cold snowy ski-slopes of the Appenine mountains, with Rome only a short car ride away.Each property will be in the OLD Abruzzo style, with attractive brick and stone walls. There are one-, two- and three-bedroomed apartments and three- or four-bedroomed villas</p>
</section>

<div class="abs promo-band"></div>
<section class="abs newsletter">
  <h2>Sign Up Newsletters</h2>
  <small>Etiam eu urna Sed porta Suspendisse quam</small>
  <div class="field">email address</div>
  <div class="btn">SUBSCRIBE</div>
</section>
<ul class="abs seasons">
  <li><svg width="20" height="20" viewBox="0 0 20 20" aria-hidden="true"><circle cx="10" cy="10" r="3.5" fill="#111"/><g fill="#111"><circle cx="10" cy="4" r="3"/><circle cx="10" cy="16" r="3"/><circle cx="4" cy="10" r="3"/><circle cx="16" cy="10" r="3"/><circle cx="5.8" cy="5.8" r="2.6"/><circle cx="14.2" cy="14.2" r="2.6"/><circle cx="14.2" cy="5.8" r="2.6"/><circle cx="5.8" cy="14.2" r="2.6"/></g><circle cx="10" cy="10" r="2" fill="#fece3e"/></svg>Photos of Spring</li>
  <li><svg width="20" height="20" viewBox="0 0 20 20" aria-hidden="true"><circle cx="10" cy="10" r="4.5" fill="none" stroke="#111" stroke-width="1.8"/><g stroke="#111" stroke-width="1.8" stroke-linecap="round"><path d="M10 1v2M10 17v2M1 10h2M17 10h2M3.6 3.6l1.4 1.4M15 15l1.4 1.4M16.4 3.6 15 5M5 15l-1.4 1.4"/></g></svg>Photos of Summer</li>
  <li><svg width="20" height="20" viewBox="0 0 20 20" aria-hidden="true"><path d="M10 1l2 4 3-1-1 4 4 1-3 3 1 3-4-1-1 5-1-5-4 1 1-3-3-3 4-1-1-4 3 1z" fill="#111"/></svg>Photos of Autumn</li>
  <li><svg width="20" height="20" viewBox="0 0 20 20" aria-hidden="true"><path d="M10 1l2.3 6.2H19l-5.4 4 2 6.6L10 14l-5.6 3.8 2-6.6L1 7.2h6.7z" fill="none" stroke="#111" stroke-width="1.6" stroke-linejoin="round"/></svg>Photos of Winter</li>
</ul>
<section class="abs book-trip" role="img" aria-label="Green park with winding path and trees">
  <div class="bar"><span>Book Trip</span><b>BOOK NOW</b></div>
</section>

<section class="abs post" style="left:42px;top:818px">
  <h2 class="section-title t-green">OLD BLOG</h2>
  <div class="img" role="img" aria-label="Lake with willow trees" style="background:linear-gradient(#dfe7ee,#6f8f3f 45%,#3d5a2a)"></div>
  <h3>Phasellus felis dolor scelerisqu</h3>
  <p>Pellentesque faucibus Ut accumsan ultricies elit Maecenas at justo id velit placerat molestie Donec</p>
</section>
<section class="abs post" style="left:231px;top:818px">
  <h2 class="section-title t-green">NEW BLOG</h2>
  <div class="img" role="img" aria-label="Pine forest with grassy floor" style="background:linear-gradient(#4a4a2e,#6f7a3f 55%,#9ab35a)"></div>
  <h3>Phasellus felis dolor scelerisqu</h3>
  <p>Pellentesque faucibus Ut accumsan ultricies elit Maecenas at justo id velit placerat molestie Donec</p>
</section>
<h2 class="abs section-title t-red" style="left:419px;top:818px">LATEST VIDEOS</h2>
<div class="abs video" style="left:420px;top:843px">
  <div class="img" role="img" aria-label="Video still of a tree-lined park path" style="background:linear-gradient(160deg,#3f8f1e,#7cc23a 55%,#a2a292)">
    <svg class="play" viewBox="0 0 30 30" aria-hidden="true"><circle cx="15" cy="15" r="14" fill="#fff"/><circle cx="15" cy="15" r="11.5" fill="#222"/><path d="M12 9.5v11l9-5.5z" fill="#fff"/></svg>
  </div>
</div>
<div class="abs video" style="left:609px;top:843px">
  <div class="img" role="img" aria-label="Video still of leaves against blue sky" style="background:linear-gradient(140deg,#4f8f2a,#2f7fd4 50%,#8ccf4a)">
    <svg class="play" viewBox="0 0 30 30" aria-hidden="true"><circle cx="15" cy="15" r="14" fill="#fff"/><circle cx="15" cy="15" r="11.5" fill="#222"/><path d="M12 9.5v11l9-5.5z" fill="#fff"/></svg>
  </div>
</div>

<section class="abs more-sites">
  <h2>Find more houses, land, properties for sale and real estate on the following sites:</h2>
  <div class="site-links">
    <span>HomesBySeaCoast (ita)</span><span>HomesBySeaCoast (uk)</span><span>HomesBySeaCoast (es)</span><span>HomesBySeaCoast (de)</span><span>VillaPortalItalia(en)</span>
    <span>VillaPortalItalia(ita)</span><span>VillaPortalItalia (bg)</span><span>VillaPortalItalia (ru)</span><span>VillaPortalItalia (de)</span><span>Casale Delle Rondini (uk)</span>
  </div>
</section>

<footer class="abs site-footer">
  <div class="abs footer-nav">Home<i>|</i>Which Reason<i>|</i>About<i>|</i>Price List<i>|</i>Videos<i>|</i>Blog<i>|</i>Photos<i>|</i>Book Trip<i>|</i>Contact</div>
  <div class="abs copyright">© 2014 Company Name.&nbsp; All right reserved.&nbsp; Term of Use</div>
  <div class="abs social-foot" aria-label="Social links"><span></span><span></span><span></span><span></span></div>
</footer>

</body>
</html>
```